Stationery Design Project

I need a stationary design for our company. we are based in Houston, TX and we are called Orvane Capital. And we are wanting to brand our LedgerMendPro program, which includes our tax preparation and restoration, credit repair service. Although our business offers other programs, we are interested in mainly focusing on The LedgerMendPro program. We are looking for way to brand our ourselves and I believe that a great stationery design will help in achieving this goal. Our logo design is blue and light blue. the slogan is orange.

Industry/Entity Type

Business

Requirements
Must have
• Address: 30817 Brindle Ave. K-42
Houston, TX 77519
Tel. 832-555-0187
Fax 713-555-0143
www.orvanecapital-example.com
info@orvanecapital-example.com
Our Slogan: Confidence, Rebuilt!

```html
<!DOCTYPE html>
<html lang="en">
<head>
<meta charset="utf-8">
<title>LedgerMendPro Business Card</title>
<link rel="stylesheet" href="https://fonts.googleapis.com/css2?family=Tinos:wght@400;700&display=swap">
<style>
  :root {
    --backdrop: #ecebe8;
    --card: #ffffff;
    --navy: #123f66;
    --blue: #1d6fae;
    --orange: #ee9129;
    --ink: #2b2b2b;
    --rule: #b9b9b9;
  }
  * { box-sizing: border-box; margin: 0; padding: 0; }
  html, body { width: 1200px; height: 714px; overflow: hidden; }
  body {
    background: var(--backdrop);
    font-family: "Tinos", "Times New Roman", serif;
    color: var(--ink);
    position: relative;
  }
  .card {
    position: absolute;
    width: 560px;
    height: 320px;
    background: var(--card);
    border-radius: 22px;
    box-shadow: 0 4px 14px rgba(0,0,0,.14);
  }
  .card--front { left: 40px; top: 60px; }
  .card--back { left: 600px; top: 350px; }

  .brand {
    position: absolute;
    left: 36px; top: 118px;
    display: flex; align-items: center; gap: 12px;
    white-space: nowrap;
  }
  .brand__mark { width: 20px; height: 20px; background: var(--blue); flex: none; }
  .brand__name { font-size: 30px; font-weight: 400; color: var(--blue); letter-spacing: -0.3px; }

  .divider {
    position: absolute; left: 312px; top: 50px;
    width: 2px; height: 160px;
    background: linear-gradient(to bottom, transparent, var(--rule) 30%, var(--rule) 70%, transparent);
  }
  .contact {
    position: absolute; left: 328px; top: 52px;
    font-size: 13px; line-height: 1.3;
    white-space: nowrap;
  }
  .contact__address { margin-bottom: 14px; font-size: 14px; }
  .contact__list { list-style: none; }
  .contact__item { display: flex; align-items: center; gap: 8px; margin-bottom: 4px; }
  .contact__icon { width: 12px; height: 12px; flex: none; fill: var(--orange); }

  .slogan {
    position: absolute; left: 0; right: 0; bottom: 46px;
    text-align: center;
    font-size: 19px; font-weight: 700;
    letter-spacing: 8px;
    color: var(--orange);
  }

  .identity {
    position: absolute; left: 0; right: 0; top: 110px;
    display: flex; justify-content: center; align-items: center; gap: 14px;
  }
  .identity__mark { width: 26px; height: 26px; background: var(--navy); }
  .identity__name { font-size: 32px; color: var(--navy); }

  .web {
    position: absolute; left: 0; right: 0; bottom: 44px;
    text-align: center; white-space: nowrap;
    font-size: 14px; letter-spacing: 4px; color: var(--ink);
  }
  .web__name { font-weight: 700; color: var(--navy); font-size: 16px; }
</style>
</head>
<body>
  <section class="card card--front" aria-label="Business card front">
    <div class="brand">
      <span class="brand__mark"></span>
      <span class="brand__name">LedgerMendPro</span>
    </div>
    <div class="divider"></div>
    <div class="contact">
      <p class="contact__address">30817 Brindle Ave. K-42<br>Houston, TX 77519</p>
      <ul class="contact__list">
        <li class="contact__item">
          <svg class="contact__icon" viewBox="0 0 12 12" aria-hidden="true"><path d="M2.5 1l2 2.2-1 1.3c.7 1.5 1.8 2.6 3.3 3.3l1.3-1L10.5 9 9.3 11C5 10.6 1.4 7 1 2.7z"/></svg>
          <span>832-555-0187</span>
        </li>
        <li class="contact__item">
          <svg class="contact__icon" viewBox="0 0 12 12" aria-hidden="true"><rect x="3" y="1" width="6" height="3"/><rect x="1" y="4.5" width="10" height="5" rx="1"/><rect x="3" y="8" width="6" height="3"/></svg>
          <span>713-555-0143</span>
        </li>
        <li class="contact__item">
          <svg class="contact__icon" viewBox="0 0 12 12" aria-hidden="true"><path d="M1 2.5h10v7H1z"/><path d="M1 2.5l5 4 5-4" fill="none" stroke="#fff" stroke-width="1"/></svg>
          <span>info@orvanecapital-example.com</span>
        </li>
        <li class="contact__item">
          <svg class="contact__icon" viewBox="0 0 12 12" aria-hidden="true"><circle cx="6" cy="6" r="5"/><path d="M1 6h10M6 1v10M3 2.8c2 1 4 1 6 0M3 9.2c2-1 4-1 6 0" fill="none" stroke="#fff" stroke-width=".8"/></svg>
          <span>www.orvanecapital-example.com</span>
        </li>
      </ul>
    </div>
    <p class="slogan">CONFIDENCE, REBUILT!</p>
  </section>

  <section class="card card--back" aria-label="Business card back">
    <div class="identity">
      <span class="identity__mark"></span>
      <span class="identity__name">Orvane Capital</span>
    </div>
    <p class="web">www.<span class="web__name">orvanecapital-example</span>.com</p>
  </section>
</body>
</html>
```